Kereru Creative Harvest Fair

We are holding our inaugural event on the 21st October 2022 on the TerraStudia campus in Palmerston North., from 10am until 2pm.The event will be a mix of Fourth year Food Technology students presenting their student projects and local producers show casing and educating around their products. The event is bought to you by CropNest along with Ashcombe Vale District Council and BRIX. The overall plan is to bring a spotlight to the amount of research and food related businesses are on this side of the river. The event will be free to enter and there will be food and products to purchase, but the main focus is on education.

```html
<!DOCTYPE html>
<html lang="en">
<head>
<meta charset="utf-8">
<title>Kereru Creative Harvest Fair</title>
<link rel="stylesheet" href="https://fonts.googleapis.com/css2?family=Montserrat:wght@400;500;600;700;800&display=swap">
<style>
  :root {
    --page: #f4f5f4;
    --white: #ffffff;
    --mint: #7fe59a;
    --green: #22b14c;
    --green-deep: #17a043;
    --orange: #f7921e;
    --orange-deep: #f26a21;
    --red: #ec1c24;
    --ink: #2b2b2b;
  }
  * { margin: 0; padding: 0; box-sizing: border-box; }
  html, body { width: 1200px; height: 1156px; overflow: hidden; }
  body {
    background: var(--page);
    font-family: "Montserrat", sans-serif;
    position: relative;
  }
  .poster {
    position: absolute;
    left: 272px; top: 132px;
    width: 656px; height: 891px;
    background: var(--white);
    overflow: hidden;
    box-shadow: 0 2px 10px rgba(0,0,0,0.08);
  }
  .hero-band {
    position: absolute; left: 0; top: 0;
    width: 656px; height: 444px;
    background: var(--mint);
  }
  .hero-art {
    position: absolute; left: 0; top: 0;
    width: 656px; height: 520px;
  }
  .entry-pill {
    position: absolute; top: 395px;
    width: 160px; height: 99px;
    background: var(--white);
    display: flex; align-items: center; justify-content: center;
    text-align: center;
    color: var(--orange);
    font-weight: 700; font-size: 24px; line-height: 1.1;
  }
  .entry-pill--left { left: 0; border-radius: 0 50px 50px 0; }
  .entry-pill--right { right: 0; border-radius: 50px 0 0 50px; }
  .event-info {
    position: absolute; left: 0; top: 528px; width: 656px;
    text-align: center;
  }
  .event-kicker {
    font-size: 24px; font-weight: 500; color: var(--ink);
    letter-spacing: 0.5px;
  }
  .event-title {
    margin-top: 2px;
    font-size: 45px; font-weight: 800;
    background: linear-gradient(90deg, var(--orange), var(--orange-deep));
    -webkit-background-clip: text; background-clip: text; color: transparent;
    line-height: 1.15;
  }
  .event-date {
    margin-top: 20px;
    font-size: 26px; font-weight: 700; color: var(--green);
  }
  .event-date .day { color: var(--red); }
  .event-date sup { font-size: 14px; }
  .event-time {
    margin-top: 6px;
    display: inline-flex; align-items: center;
    font-size: 23px; font-weight: 700; line-height: 1;
  }
  .event-time .label { color: var(--red); padding-right: 10px; border-right: 2px solid var(--ink); }
  .event-time .value { color: var(--green); padding-left: 10px; }
  .event-venue {
    margin-top: 22px;
    font-size: 22px; font-weight: 800; color: var(--green-deep);
    line-height: 1.6;
  }
  .sponsor-band {
    position: absolute; left: 0; bottom: 0;
    width: 656px; height: 84px;
    background: var(--green);
    color: var(--white);
    text-align: center;
  }
  .sponsor-intro {
    padding-top: 8px;
    font-size: 8px; font-weight: 700; letter-spacing: 0.3px;
  }
  .sponsor-list {
    margin-top: 18px;
    display: flex; justify-content: center; gap: 58px;
    font-size: 19px; font-weight: 700;
  }
</style>
</head>
<body>
  <main class="poster">
    <div class="hero-band"></div>

    <svg class="hero-art" viewBox="0 0 492 390" xmlns="http://www.w3.org/2000/svg">
      <defs>
        <linearGradient id="labTone" x1="0" y1="0" x2="1" y2="1">
          <stop offset="0" stop-color="#e9dcc2"/>
          <stop offset="1" stop-color="#f3f3f1"/>
        </linearGradient>
        <linearGradient id="truckTone" x1="0" y1="0" x2="0" y2="1">
          <stop offset="0" stop-color="#3f7a3a"/>
          <stop offset="0.55" stop-color="#e8b52a"/>
          <stop offset="1" stop-color="#b9bcc0"/>
        </linearGradient>
        <linearGradient id="chefTone" x1="0" y1="0" x2="1" y2="1">
          <stop offset="0" stop-color="#9a8f86"/>
          <stop offset="1" stop-color="#f1eeea"/>
        </linearGradient>
      </defs>
      <polygon points="92,-55 242,95 92,245 -58,95" fill="url(#labTone)" role="img" aria-label="Photo of a food technology student in a lab coat"/>
      <polygon points="400,-55 550,95 400,245 250,95" fill="url(#chefTone)" role="img" aria-label="Photo of a smiling chef in whites and toque"/>
      <polygon points="247,113 384,250 247,387 110,250" fill="url(#truckTone)" stroke="#ffffff" stroke-width="3" role="img" aria-label="Photo of colourful food trucks parked in a row"/>
      <path d="M157,0 H337 L254,83 Q247,90 240,83 Z" fill="var(--green)"/>
      <text x="247" y="16" text-anchor="middle" font-family="Montserrat, sans-serif" font-size="8.5" font-weight="500" fill="#ffffff">KERERU CREATIVE</text>
      <text x="247" y="32" text-anchor="middle" font-family="Montserrat, sans-serif" font-size="11" font-weight="700" fill="#ffffff">HARVEST</text>
      <text x="247" y="47" text-anchor="middle" font-family="Montserrat, sans-serif" font-size="11" font-weight="700" fill="#ffffff">FAIR</text>
    </svg>

    <div class="entry-pill entry-pill--left">FREE<br>ENTRY</div>
    <div class="entry-pill entry-pill--right">FREE<br>ENTRY</div>

    <section class="event-info">
      <p class="event-kicker">KERERU CREATIVE</p>
      <h1 class="event-title">HARVEST FAIR</h1>
      <p class="event-date"><span class="day">21<sup>st</sup></span> OCTOBER 2022</p>
      <p class="event-time"><span class="label">TIME</span><span class="value">Sharp 10:00 AM</span></p>
      <p class="event-venue">TERRASTUDIA CAMPUS<br>IN PALMERSTON NORTH</p>
    </section>

    <footer class="sponsor-band">
      <p class="sponsor-intro">THE EVENT IS BROUGHT TO YOU BY</p>
      <div class="sponsor-list">
        <span class="sponsor">CropNest</span>
        <span class="sponsor">Ashcombe Vale</span>
        <span class="sponsor">BRIX</span>
      </div>
    </footer>
  </main>
</body>
</html>
```